Gallant Meridian Informational Sheet

I need a one page informational sheet (advertisement) for a horse called Gallant Meridian. It should have the name Gallant Meridian and the content below. It needs to be eye-catching. I have attached 3 examples of what these advertisements look like so it's easier to create. I've also attached 2 pictures of the horse which should both be used in the advertisement.

Here are the bullet points:

- Son of Stormy Bastion with total progeny earnings over 13 million dollars
- Ranks among West Virginia top 3 active sires by progeny earnings 2019
- In 9 crops of racing age, has sired 200 winners from 275 starters
- Sired Don Tallarico who earned over $800k racing from age 2 to 7.
- Won 3 of 4 lifetime starts

stands at stud for $1000 at Ashgrove Farm near Charles Town
Call Dale Whitcomb - (304) 555-0193

Target Market(s)

Thoroughbred racing people interested in breeding

Requirements
Must have
• Unique and creative. The name of the horse Gallant Meridian should be clear and bold, the picture should also be prominent.
Should not have
• Cartoon like, whimsical

```html
<!DOCTYPE html>
<html lang="en">
<head>
<meta charset="utf-8">
<title>Gallant Meridian – Stallion Sheet</title>
<link rel="stylesheet" href="https://fonts.googleapis.com/css2?family=League+Gothic&family=Oswald:wght@300;500&family=Montserrat:wght@500;800&display=swap">
<style>
  :root {
    --ink: #0e0e0e;
    --paper: #ffffff;
    --gold: #f2c23f;
    --orange: #ec8a4b;
    --green: #a9c94c;
    --green-dark: #9bbd3f;
    --bay: #7a3b1c;
    --bay-light: #b0602e;
    --bay-deep: #4a2412;
    --brick: #b8633f;
    --stable: #3f4c44;
  }
  * { margin: 0; padding: 0; box-sizing: border-box; }
  html, body { width: 848px; height: 1200px; overflow: hidden; background: var(--paper); }
  .sheet { position: relative; width: 848px; height: 1200px; overflow: hidden; background: var(--ink); }

  .hero-photo {
    position: absolute; left: 0; top: 0; width: 463px; height: 1090px;
    background:
      linear-gradient(180deg, var(--brick) 0 52px, transparent 52px),
      radial-gradient(ellipse 62% 48% at 52% 58%, var(--bay-light) 0%, var(--bay) 55%, transparent 80%),
      radial-gradient(ellipse 80% 40% at 40% 95%, var(--bay) 0%, var(--bay-deep) 70%, transparent 100%),
      linear-gradient(180deg, #56625a 5%, var(--stable) 40%, #2f3a33 100%);
  }

  .info-panel { position: absolute; left: 463px; top: 0; width: 385px; height: 1090px; background: var(--ink); }

  .green-band {
    position: absolute; left: 0; top: 820px; width: 848px; height: 270px;
    clip-path: polygon(0 246px, 848px 14px, 848px 270px, 0 270px);
    background: repeating-linear-gradient(90deg, var(--green) 0 9px, var(--green-dark) 9px 18px);
  }

  .side-photo {
    position: absolute; left: 475px; top: 822px; width: 337px; height: 268px;
    background:
      radial-gradient(ellipse 42% 26% at 58% 42%, var(--bay-light) 0%, var(--bay) 70%, transparent 100%),
      radial-gradient(ellipse 40% 30% at 55% 80%, rgba(40,22,12,.55) 0%, transparent 100%);
  }

  .headline { position: absolute; left: 490px; top: 0; width: 336px; height: 470px; font-family: "League Gothic", sans-serif; font-weight: 400; line-height: 1; white-space: nowrap; }
  .headline span { position: absolute; left: 0; display: block; transform-origin: left top; }
  .headline .kicker { top: 78px; color: var(--orange); font-size: 92px; }
  .headline .name { color: var(--gold); text-transform: uppercase; font-size: 114px; transform: scaleY(1.32); }
  .headline .name-first { top: 180px; }
  .headline .name-last { top: 318px; }

  .highlights { position: absolute; left: 530px; top: 510px; width: 290px; list-style: none; font-family: "Oswald", sans-serif; font-weight: 300; color: var(--paper); font-size: 18px; line-height: 1.25; }
  .highlights li { position: relative; padding-left: 28px; margin-bottom: 19px; }
  .highlights li svg { position: absolute; left: 0; top: 1px; width: 21px; height: 21px; }
  .highlights strong { font-weight: 500; text-transform: uppercase; }

  .stud-footer {
    position: absolute; left: 0; top: 1090px; width: 848px; height: 60px; background: var(--ink);
    color: var(--paper); font-family: "Montserrat", sans-serif; font-weight: 500; font-size: 17px;
    text-align: center; line-height: 1.35; padding-top: 6px;
  }
  .stud-footer strong { font-weight: 800; text-transform: uppercase; }
  .stud-footer .fee { text-transform: none; }
  .base-strip { position: absolute; left: 0; top: 1150px; width: 848px; height: 50px; background: repeating-linear-gradient(90deg, var(--green) 0 9px, var(--green-dark) 9px 18px); }
</style>
</head>
<body>
<main class="sheet">
  <div class="hero-photo" role="img" aria-label="Head and neck portrait of Gallant Meridian, a bay stallion in a leather halter, in front of a stable"></div>
  <section class="info-panel"></section>
  <div class="green-band"></div>
  <div class="side-photo" role="img" aria-label="Full-body side view of Gallant Meridian standing"></div>

  <h1 class="headline">
    <span class="kicker">Meet the best</span>
    <span class="name name-first">Gallant</span>
    <span class="name name-last">Meridian</span>
  </h1>

  <ul class="highlights">
    <li><svg viewBox="0 0 24 24"><path fill="#f2c23f" d="M12 1.5l3.1 6.9 7.4.7-5.6 5 1.7 7.4L12 17.6 5.4 21.5l1.7-7.4-5.6-5 7.4-.7z"/></svg>Son of <strong>Stormy Bastion</strong> with total progeny earnings over 13 million dollars</li>
    <li><svg viewBox="0 0 24 24"><path fill="#f2c23f" d="M12 1.5l3.1 6.9 7.4.7-5.6 5 1.7 7.4L12 17.6 5.4 21.5l1.7-7.4-5.6-5 7.4-.7z"/></svg>Ranks among West Virginia top 3 active sires by progeny earnings 2019</li>
    <li><svg viewBox="0 0 24 24"><path fill="#f2c23f" d="M12 1.5l3.1 6.9 7.4.7-5.6 5 1.7 7.4L12 17.6 5.4 21.5l1.7-7.4-5.6-5 7.4-.7z"/></svg>In 9 crops of racing age, has sired 200 winners from 275 starters</li>
    <li><svg viewBox="0 0 24 24"><path fill="#f2c23f" d="M12 1.5l3.1 6.9 7.4.7-5.6 5 1.7 7.4L12 17.6 5.4 21.5l1.7-7.4-5.6-5 7.4-.7z"/></svg>Sired <strong>Don Tallarico</strong> who earned over $800k racing from age 2 to 7.</li>
    <li><svg viewBox="0 0 24 24"><path fill="#f2c23f" d="M12 1.5l3.1 6.9 7.4.7-5.6 5 1.7 7.4L12 17.6 5.4 21.5l1.7-7.4-5.6-5 7.4-.7z"/></svg>Won 3 of 4 lifetime starts</li>
  </ul>

  <footer class="stud-footer">
    <p>Stands at stud for <strong class="fee">$1000</strong> at <strong>Ashgrove Farm</strong> near Charles Town</p>
    <p>Call <strong>Dale Whitcomb</strong> - (304) 555-0193</p>
  </footer>
  <div class="base-strip"></div>
</main>
</body>
</html>
```